FURLOW MEADOW Pet Resorts Outdoor Signage

4 x 8 outdoor signage design for our two locations

Target Market(s)

Existing and New Customers

Industry/Entity Type

Pet Care

Font styles to use
Sans Serif

Colors

Designer to choose colors to be used in the design.

```html
<!DOCTYPE html>
<html lang="en">
<head>
<meta charset="utf-8">
<title>FURLOW MEADOW Pet Resort – Outdoor Sign</title>
<link rel="stylesheet" href="https://fonts.googleapis.com/css2?family=Roboto:wght@500;700&family=Roboto+Condensed:wght@700&display=swap">
<style>
  :root {
    --page: #e9e9ec;
    --navy: #1b1550;
    --teal: #4a93a6;
    --slate: #6e6d74;
    --white: #ffffff;
  }
  * { margin: 0; padding: 0; box-sizing: border-box; }
  html, body {
    width: 1200px; height: 999px; overflow: hidden;
    background: var(--page);
    font-family: "Roboto", Arial, sans-serif;
  }
  .sign {
    position: absolute; left: 330px; top: 30px;
    width: 540px; height: 940px;
    background: var(--navy);
    color: var(--white);
  }
  .brand {
    position: absolute; top: 95px; left: 0; right: 0;
    text-align: center;
    font-weight: 700; font-size: 74px; line-height: 1.02;
    letter-spacing: 1px;
    color: var(--slate);
  }
  .headline {
    position: absolute; top: 358px; left: 0; right: 0;
    text-align: center;
    font-weight: 700; font-size: 42px; letter-spacing: 0.5px;
  }
  .tagline {
    position: absolute; top: 420px; left: 0; right: 0;
    text-align: center;
    font-family: "Roboto Condensed", "Arial Narrow", sans-serif;
    font-weight: 700; font-size: 39px; letter-spacing: 0.5px;
    color: var(--teal);
  }
  .services {
    position: absolute; top: 490px; left: 80px;
    list-style: none;
  }
  .services li {
    display: flex; align-items: center;
    height: 51.5px;
    font-weight: 700; font-size: 27px;
  }
  .services svg { width: 34px; height: 34px; margin-right: 27px; flex: none; }
  .phone {
    position: absolute; top: 765px; left: 0; right: 0;
    text-align: center;
    font-weight: 700; font-size: 58px; letter-spacing: 0.5px;
  }
  .web-band {
    position: absolute; top: 850px; left: -6px; right: 0;
    height: 54px;
    background: var(--teal);
    display: flex; align-items: center; justify-content: center;
    font-weight: 700; font-size: 28px; letter-spacing: 4px;
  }
</style>
</head>
<body>
<svg width="0" height="0" style="position:absolute">
  <defs>
    <symbol id="bone-icon" viewBox="0 0 34 34">
      <circle cx="17" cy="17" r="17" fill="#4a93a6"/>
      <g fill="#1b1550">
        <rect x="10" y="14.5" width="14" height="5"/>
        <circle cx="9.5" cy="13.5" r="3"/>
        <circle cx="9.5" cy="20.5" r="3"/>
        <circle cx="24.5" cy="13.5" r="3"/>
        <circle cx="24.5" cy="20.5" r="3"/>
      </g>
    </symbol>
  </defs>
</svg>

<main class="sign">
  <div class="brand">FURLOW<br>MEADOW</div>
  <h1 class="headline">PET RESORT</h1>
  <p class="tagline">ALL BREED FRIENDLY</p>
  <ul class="services">
    <li><svg><use href="#bone-icon"/></svg>Boarding</li>
    <li><svg><use href="#bone-icon"/></svg>Daycare</li>
    <li><svg><use href="#bone-icon"/></svg>Training</li>
    <li><svg><use href="#bone-icon"/></svg>Full-Service Salon</li>
    <li><svg><use href="#bone-icon"/></svg>Pet Taxi &amp; More</li>
  </ul>
  <p class="phone">905-555-0148</p>
  <div class="web-band">www.furlowmeadow.ca</div>
</main>
</body>
</html>
```